K7 Morvane Advisory Partners Ltd - Website Design

We already have a company logo. We need a website created for our consulting agency.
Refer to attached files for logo and website content.
We would also be open to any additional recommendations.
Industry/Entity Type
Finance And Accounting
Coding
Coded - Design and coding required
Number of Pages Required
1 page
Font styles to use
Serif
Colors
3377b5
b868aa
33b8a4
Requirements
Must have
- Company Logo, name and who we are.

```html
<!DOCTYPE html>
<html lang="en">
<head>
<meta charset="utf-8">
<title>K7 Morvane Advisory Partners Ltd</title>
<link href="https://fonts.googleapis.com/css2?family=Poppins:wght@400;500;600;700&family=Open+Sans:wght@400;600&display=swap" rel="stylesheet">
<style>
:root{
  --blue:#3377b5;
  --navy:#2a2f7a;
  --purple:#b868aa;
  --teal:#33b8a4;
  --grey:#ececec;
  --ink:#222;
  --muted:#666;
  --white:#fff;
}
*{margin:0;padding:0;box-sizing:border-box}
html,body{width:1200px;height:4728px;overflow:hidden}
body{font-family:"Open Sans",Arial,sans-serif;color:var(--ink);background:var(--white);position:relative}
h1,h2,h3,h4,.brand,.nav,.btn{font-family:"Poppins",Arial,sans-serif}
section,header,footer{position:absolute;left:0;width:1200px}
.btn{display:inline-block;background:var(--purple);color:#fff;border-radius:40px;font-weight:500;text-align:center}
.btn-outline{display:inline-block;border:2px solid #777;border-radius:30px;font-family:"Poppins",sans-serif;font-size:15px;font-weight:600;color:#333;padding:6px 26px}

/* header */
.site-header{top:0;height:84px;background:var(--white);z-index:3}
.brand{position:absolute;left:36px;top:14px;display:flex;align-items:center;gap:10px;font-size:22px;font-weight:600;color:var(--navy)}
.brand-dot{width:34px;height:34px;border-radius:50%;background:var(--navy)}
.nav{position:absolute;left:480px;top:32px;display:flex;gap:34px;font-size:17px;font-weight:500;color:#222}
.estimate{position:absolute;right:36px;top:18px;text-align:left;font-family:"Poppins",sans-serif}
.estimate small{display:block;font-size:14px;font-weight:600}
.estimate strong{font-size:24px;color:var(--blue);font-weight:600}

/* hero */
.hero{top:84px;height:720px}
.hero-photo{position:absolute;inset:0;background:linear-gradient(120deg,#c9d2de,#e9e2dc 45%,#9fb3c9);}
.hero-tint{position:absolute;inset:0;background:linear-gradient(180deg,rgba(255,255,255,0) 40%,rgba(51,119,181,.45))}
.hero h1{position:absolute;left:0;width:100%;top:440px;text-align:center;color:#fff;font-size:76px;font-weight:500}
.hero-curve{position:absolute;left:0;bottom:-2px}

/* welcome */
.welcome{top:804px;height:564px}
.welcome-mark{position:absolute;left:110px;top:110px;width:380px;height:300px;display:flex;align-items:center;justify-content:center;font-family:"Poppins",sans-serif;font-size:40px;font-weight:600;color:#c9d3e3}
.welcome-text{position:absolute;left:560px;top:84px;width:470px}
.welcome-text h2{font-size:38px;line-height:1.15;font-weight:700;color:var(--ink)}
.welcome-text p{margin-top:18px;font-size:14.5px;line-height:1.6}
.welcome-text .btn{margin-top:34px;font-size:17px;padding:12px 30px}

/* services */
.services{top:1368px;height:1060px;background:var(--grey)}
.section-title{position:absolute;width:100%;text-align:center;font-size:46px;font-weight:600;color:var(--navy)}
.services .section-title{top:72px}
.service-card{position:absolute;width:306px;height:262px;background:#fff;box-shadow:0 4px 14px rgba(0,0,0,.12);text-align:center;padding-top:0}
.service-icon{width:86px;height:86px;border-radius:50%;margin:-20px auto 0;display:flex;align-items:center;justify-content:center}
.service-card h3{font-size:17px;font-weight:600;margin-top:14px;letter-spacing:.3px}
.service-card p{font-size:13.5px;line-height:1.45;margin:10px 26px 0}
.service-card .btn-outline{margin-top:16px}
.query{position:absolute;left:160px;top:890px;font-family:"Poppins",sans-serif;font-size:30px;line-height:1.2;color:#222;font-weight:500}
.query strong{font-weight:700}
.query span{color:var(--teal);font-weight:600}
.services .btn{position:absolute;left:848px;top:898px;font-size:19px;padding:12px 44px}

/* innovate */
.innovate{top:2428px;height:720px}
.innovate-bg{position:absolute;inset:0;background:linear-gradient(120deg,#2d6aa8,var(--blue) 50%,#5d8fc0)}
.innovate-photo{position:absolute;left:150px;top:150px;width:420px;height:420px;border-radius:50%;background:linear-gradient(135deg,#dfe6ee,#8ea6bf);border:8px solid var(--teal)}
.innovate-text{position:absolute;left:610px;top:218px;width:480px;color:#fff}
.innovate-text h2{font-size:32px;line-height:1.2;font-weight:600}
.innovate-text p{margin-top:20px;font-size:14.5px;line-height:1.6}

/* blog */
.blog{top:3148px;height:652px}
.blog .section-title{top:8px}
.blog-card{position:absolute;top:110px;width:290px;height:380px;background:#fff;box-shadow:0 4px 14px rgba(0,0,0,.12)}
.blog-img{height:172px}
.blog-body{padding:18px 20px}
.blog-body small{font-size:12px;color:var(--muted)}
.blog-body h4{font-size:19px;line-height:1.25;font-weight:600;margin-top:6px}
.blog-body p{font-size:13.5px;line-height:1.4;color:var(--muted);margin-top:8px}
.blog-body a{display:block;margin-top:10px;font-size:13px;color:var(--navy);text-decoration:underline;font-weight:600}
.blog .btn{position:absolute;left:500px;top:550px;font-size:17px;padding:12px 40px}

/* testimonial */
.testimonial{top:3800px;height:560px;background:#f5f5f5}
.testimonial .section-title{top:100px;font-size:40px;color:var(--blue)}
.title-rule{position:absolute;left:480px;top:160px;width:240px;height:3px;background:var(--blue)}
.client-photo{position:absolute;left:262px;top:280px;width:164px;height:164px;border-radius:50%;background:linear-gradient(135deg,#d7c7b9,#8a9db3);border:5px solid #fff;box-shadow:0 4px 12px rgba(0,0,0,.15);z-index:2}
.quote-card{position:absolute;left:360px;top:270px;width:560px;height:236px;background:#fff;box-shadow:0 4px 14px rgba(0,0,0,.1);text-align:center;padding:30px 90px 0}
.quote-card p{font-size:14.5px;line-height:1.5;margin-top:14px}
.quote-card h4{margin-top:12px;color:var(--purple);font-size:18px;font-weight:500}
.slider-arrows{position:absolute;left:800px;top:470px;display:flex}
.slider-arrows span{width:44px;height:44px;display:flex;align-items:center;justify-content:center}

/* footer */
.site-footer{top:4360px;height:368px;background:var(--blue);color:#fff}
.footer-brand{position:absolute;left:150px;top:70px;font-family:"Poppins",sans-serif;font-size:28px;font-weight:600;display:flex;align-items:center;gap:10px}
.footer-brand i{width:30px;height:30px;background:#fff;border-radius:50%}
.footer-col{position:absolute;top:56px;font-size:13.5px;line-height:2}
.footer-col h4{font-size:14px;font-weight:600}
.footer-col a{display:block;color:#fff;text-decoration:underline}
.footer-map{position:absolute;left:790px;top:60px;width:290px;height:116px;background:linear-gradient(135deg,#e7eef2,#cfdfe6)}
.socials{position:absolute;left:520px;top:250px;display:flex;gap:14px}
.socials span{width:28px;height:28px;border-radius:50%;border:2px solid #fff}
.copyright{position:absolute;width:100%;top:308px;text-align:center;font-size:13px}
</style>
</head>
<body>

<header class="site-header">
  <div class="brand"><span class="brand-dot"></span>K7 Morvane</div>
  <nav class="nav"><span>HOME</span><span>ABOUT</span><span>SERVICES</span><span>BLOG</span><span>CONTACT</span></nav>
  <div class="estimate"><small>FREE ESTIMATES</small><strong>(000) 888 - 888</strong></div>
</header>

<section class="hero">
  <div class="hero-photo" role="img" aria-label="Photo of advisors reviewing finances with a couple at a desk"></div>
  <div class="hero-tint"></div>
  <h1>Financial Planners</h1>
  <svg class="hero-curve" width="1200" height="90" viewBox="0 0 1200 90" aria-hidden="true">
    <path d="M0 20 Q600 110 1200 20 L1200 90 L0 90Z" fill="#fff"/>
    <path d="M0 20 Q600 110 1200 20" fill="none" stroke="#2a2f7a" stroke-width="4"/>
  </svg>
</section>

<section class="welcome">
  <div class="welcome-mark">K7 Morvane</div>
  <div class="welcome-text">
    <h2>WELCOME TO<br>K7 MORVANE ADVISORY</h2>
    <p>We are a finance and accounting consultancy helping owners run healthier businesses. Our team brings clear advice on bookkeeping, planning, grants and growth, so you can make confident decisions with numbers you trust. From first startup budgets to major acquisitions, we stay beside you at every step and keep the details simple.</p>
    <span class="btn">Learn More</span>
  </div>
</section>

<section class="services">
  <h2 class="section-title">Services Offered?</h2>

  <div class="service-card" style="left:108px;top:180px">
    <div class="service-icon" style="background:var(--purple)"><svg width="40" height="40" viewBox="0 0 40 40" fill="none" stroke="#fff" stroke-width="3"><rect x="9" y="5" width="22" height="30" rx="2"/><path d="M14 13h12M14 20h12M14 27h7"/></svg></div>
    <h3>ACCOUNTING</h3>
    <p>Accurate records and clear reports that keep your business ready for any review.</p>
    <span class="btn-outline">LEARN MORE</span>
  </div>
  <div class="service-card" style="left:446px;top:180px">
    <div class="service-icon" style="background:var(--teal)"><svg width="40" height="40" viewBox="0 0 40 40" fill="none" stroke="#fff" stroke-width="3"><path d="M8 6h16l8 8v20H8z"/><path d="M14 20h12M14 27h12"/></svg></div>
    <h3>BOOKKEEPING</h3>
    <p>Tidy monthly books, reconciled accounts and simple summaries you can act on.</p>
    <span class="btn-outline">LEARN MORE</span>
  </div>
  <div class="service-card" style="left:784px;top:180px">
    <div class="service-icon" style="background:var(--blue)"><svg width="40" height="40" viewBox="0 0 40 40" fill="none" stroke="#fff" stroke-width="3"><circle cx="20" cy="20" r="13"/><path d="M20 12v16M15 16h8a3 3 0 010 6h-6a3 3 0 000 6h8"/></svg></div>
    <h3>FINANCIAL MANAGEMENT</h3>
    <p>Budgets, cash flow and forecasts built to guide smart everyday decisions.</p>
    <span class="btn-outline">LEARN MORE</span>
  </div>
  <div class="service-card" style="left:108px;top:500px">
    <div class="service-icon" style="background:var(--blue)"><svg width="40" height="40" viewBox="0 0 40 40" fill="none" stroke="#fff" stroke-width="3"><path d="M6 16L20 7l14 9M9 16v14M17 16v14M23 16v14M31 16v14M6 33h28"/></svg></div>
    <h3>GOVERNMENT GRANTS</h3>
    <p>We find suitable programs and prepare strong applications on your behalf.</p>
    <span class="btn-outline">LEARN MORE</span>
  </div>
  <div class="service-card" style="left:446px;top:500px">
    <div class="service-icon" style="background:var(--purple)"><svg width="40" height="40" viewBox="0 0 40 40" fill="none" stroke="#fff" stroke-width="3"><path d="M7 31l9-9 6 6 11-13"/><path d="M26 15h7v7"/></svg></div>
    <h3>STRATEGY</h3>
    <p>Practical plans that link your goals to numbers and clear next steps.</p>
    <span class="btn-outline">LEARN MORE</span>
  </div>
  <div class="service-card" style="left:784px;top:500px">
    <div class="service-icon" style="background:var(--teal)"><svg width="40" height="40" viewBox="0 0 40 40" fill="none" stroke="#fff" stroke-width="3"><circle cx="14" cy="20" r="8"/><circle cx="26" cy="20" r="8"/></svg></div>
    <h3>MERGERS AND ACQUISITIONS</h3>
    <p>Valuation, due diligence and deal support from first talk to closing.</p>
    <span class="btn-outline">LEARN MORE</span>
  </div>

  <p class="query">If you want to know more, submit a query<br><strong>or call</strong> <span>888 8888 888</span></p>
  <span class="btn">Send Request</span>
</section>

<section class="innovate">
  <div class="innovate-bg" role="img" aria-label="Blue-toned photo of a business meeting behind the section"></div>
  <svg style="position:absolute;left:0;top:-2px" width="1200" height="90" viewBox="0 0 1200 90" aria-hidden="true"><path d="M0 0H1200V30Q600 110 0 30Z" fill="#ececec"/></svg>
  <div class="innovate-photo" role="img" aria-label="Photo of a professional working at a laptop"></div>
  <div class="innovate-text">
    <h2>WE HELP BUSINESS INNOVATE<br>AND GROW</h2>
    <p>Growth needs more than hard work. It needs clear figures, steady planning and honest advice. We work with owners to spot new chances, cut waste and build systems that scale. Our advisors turn complex finances into simple choices, helping your team move forward with focus, confidence and a plan that lasts for years.</p>
  </div>
</section>

<section class="blog">
  <h2 class="section-title">Latest Blog</h2>
  <article class="blog-card" style="left:132px">
    <div class="blog-img" role="img" aria-label="Photo of a laptop on a dark desk" style="background:linear-gradient(135deg,#3a2a6a,#b44a8a)"></div>
    <div class="blog-body"><small>By Admin</small><h4>Five habits of companies with healthy cash flow</h4><p>Simple routines that keep money moving and bills paid on time.</p><a>Read More</a></div>
  </article>
  <article class="blog-card" style="left:455px">
    <div class="blog-img" role="img" aria-label="Photo of a city skyline at dusk" style="background:linear-gradient(135deg,#1f3e6e,#8aa9cc)"></div>
    <div class="blog-body"><small>By Admin</small><h4>How to prepare your books for year end review</h4><p>A short checklist to make closing the year calm and quick.</p><a>Read More</a></div>
  </article>
  <article class="blog-card" style="left:778px">
    <div class="blog-img" role="img" aria-label="Photo of a man in a suit at an office desk" style="background:linear-gradient(135deg,#c9ccd2,#5d6672)"></div>
    <div class="blog-body"><small>By Admin</small><h4>Choosing the right grant for your next project</h4><p>What funders look for and how to present your case well.</p><a>Read More</a></div>
  </article>
  <span class="btn">View all Blogs</span>
</section>

<section class="testimonial">
  <h2 class="section-title">Client Testimonial</h2>
  <div class="title-rule"></div>
  <div class="client-photo" role="img" aria-label="Portrait photo of a client"></div>
  <div class="quote-card">
    <svg width="44" height="34" viewBox="0 0 44 34" fill="var(--purple)"><path d="M0 34V18C0 8 6 2 16 0l2 5c-6 2-9 6-9 11h9v18zM26 34V18c0-10 6-16 16-18l2 5c-6 2-9 6-9 11h9v18z"/></svg>
    <p>Their team made our finances easy to follow and helped us secure funding we had missed for years. Clear, friendly advice.</p>
    <h4>Elian Marsh</h4>
  </div>
  <div class="slider-arrows">
    <span style="background:#fff"><svg width="14" height="14" viewBox="0 0 14 14"><path d="M9 2L4 7l5 5" stroke="#333" stroke-width="2.5" fill="none"/></svg></span>
    <span style="background:var(--teal)"><svg width="14" height="14" viewBox="0 0 14 14"><path d="M5 2l5 5-5 5" stroke="#fff" stroke-width="2.5" fill="none"/></svg></span>
  </div>
</section>

<footer class="site-footer">
  <div class="footer-brand"><i></i>K7 Morvane</div>
  <div class="footer-col" style="left:384px"><h4>HOME</h4><h4>ABOUT US</h4><h4>OUR WORK</h4><h4>CONTACT</h4></div>
  <div class="footer-col" style="left:512px"><h4>SERVICES</h4><a>Tax Filing</a><a>Payroll Support</a><a>Advisory</a></div>
  <div class="footer-col" style="left:672px"><h4>QUICK LINKS</h4><a>FAQ</a><a>Reviews</a><a>Sitemap</a></div>
  <div class="footer-map" role="img" aria-label="Map showing the office location"></div>
  <div class="socials"><span></span><span></span><span></span><span></span></div>
  <p class="copyright">© 2020 K7 Morvane Advisory Partners Ltd. All Rights are Reserved.</p>
</footer>

</body>
</html>
```